Professional Lighting Providers - Web Design

We need a web design to showcase our ability to provide lighting design and equipment to those who are in need of lighting equipment.

Our 4 markets are:
Broadcasting - Public and Commercial
Education - ISD wide, and private schools
Government - National News, Chamber videos, Press Releases
Religious - Sermon Recording, etc.

We provide lighting products, design consultations(how lights are setup and such), and custom light work.

We want the home page to be setup in a way that someone in one of the 4 markets can drill down into the site. Meaning they are greeted on the home page with 4 large icons or pictures for each market and then they can go farther into the site. We also want a top navigation to be preset so people who are just looking for lighting can also browse our products.

Logo colors are not as they appear on our current website.
#383388 is our current logo color, please also see attachment of logo. In addition, we are just "Bright Harbor - Lighting Systems". We dropped the RJ7 out of our name so please don't use it in the concept.

Our Current Site is http://rj7-example.com/index.asp.
We don't have set colors but we know we do not want reds or yellows.

The design should be simple, not cluttered, and not artsy, not fun, but very serious.

Requirements
Must have
• Image banner/slider at the top that slides our 4 products.
Also need to have a form on the home page that will convert visitors to subscribers for a newsletter. Also on every page we want a form were people can send an email off to us asking questions.

```html
<!DOCTYPE html>
<html lang="en">
<head>
<meta charset="utf-8">
<title>Bright Harbor Lighting Systems</title>
<link rel="stylesheet" href="https://fonts.googleapis.com/css2?family=Arimo:wght@400;700&family=Gelasio:ital,wght@0,400;0,700;1,400;1,700&family=Noto+Sans:wght@400;700&display=swap">
<style>
:root{
  --brand:#383388;
  --sky:#1a8ad8;
  --navy:#0f2d62;
  --navy-deep:#0a2452;
  --green-top:#a6d742;
  --green-bottom:#5c9910;
  --ink:#333;
  --muted:#6b6b6b;
  --heading:#27307a;
}
*{box-sizing:border-box;margin:0;padding:0}
html,body{width:1010px;height:1200px;overflow:hidden;background:#fff}
body{font-family:"Arimo",Arial,sans-serif;color:var(--ink);position:relative}
.page{position:absolute;left:0;top:0;width:940px;height:1116px;overflow:hidden;transform:scale(1.07446);transform-origin:0 0;background:linear-gradient(#f4f4f4,#fff 140px)}
.abs{position:absolute}
/* header */
.brand{left:62px;top:18px;display:flex;align-items:center;gap:10px}
.brand-mark{width:34px;height:34px;background:var(--brand)}
.brand-name{font-weight:700;font-size:22px;color:var(--brand);line-height:1.1}
.brand-name small{display:block;font-size:14px;letter-spacing:2px}
.quote-btn{left:730px;top:0;width:177px;height:23px;border-radius:0 0 5px 5px;background:linear-gradient(#8fd6fb,#3eaee8);border:1px solid #2a8fc7;font-weight:700;font-size:14px;color:#0d2a55;display:flex;align-items:center;justify-content:center;gap:8px;letter-spacing:.5px}
.quote-btn svg{width:17px;height:17px}
.phone{left:744px;top:36px;display:flex;align-items:center;gap:8px;font-weight:700;font-size:16px;color:var(--sky)}
/* nav */
.nav{left:45px;top:93px;width:871px;height:38px;border-radius:8px 8px 0 0;background:linear-gradient(var(--green-top),var(--green-bottom));display:flex}
.nav a{display:flex;align-items:center;justify-content:center;font-size:12.5px;color:#1e2a08;text-decoration:none;border-right:1px solid #5a8c14;box-shadow:1px 0 0 #b8e06a;white-space:nowrap}
.nav a:last-child{border:0;box-shadow:none}
.nav a.active{color:#fff;background:linear-gradient(#8cc82d,#4f8a0b);border-radius:8px 0 0 0}
.nav-rule{left:0;top:131px;width:940px;height:4px;border-top:2px solid #555;border-bottom:1px solid #bbb}
/* welcome */
.welcome{left:52px;top:152px;width:350px}
.welcome h1{font-family:"Gelasio",serif;font-weight:400;font-size:13px;color:#555;border-bottom:1px solid #ddd;padding-bottom:6px;white-space:nowrap}
.welcome h1 span{font-size:18.5px;color:var(--sky)}
.pedigree{font-family:"Gelasio",serif;font-style:italic;font-weight:400;font-size:12px;line-height:1.35;margin-top:12px}
.pedigree .lead{font-weight:700;color:var(--heading)}
.pedigree .claim{color:var(--sky)}
.welcome p.body{font-size:10.2px;line-height:15.5px;color:#444;margin-top:12px}
.welcome-rule{left:49px;top:388px;width:353px;height:2px;background:linear-gradient(90deg,#fff,#ccc,#fff)}
.btn-small{display:flex;align-items:center;justify-content:center;gap:4px;color:#fff;font-size:9px;border-radius:4px;background:linear-gradient(#3a6cc1,#0d2e72);border:1px solid #0b2358}
.read-more{left:329px;top:401px;width:70px;height:18px}
.slider{left:413px;top:150px;width:484px;height:277px;background:#fff;box-shadow:0 2px 8px rgba(0,0,0,.35)}
.slide-photo{left:7px;top:8px;width:469px;height:260px;background:linear-gradient(135deg,#3a2a10,#b27424 30%,#d99a3c 45%,#4a5f8c 55%,#8a3030 75%,#1a1208)}
.arrow{top:263px;width:47px;height:55px;border-radius:5px;background:linear-gradient(#3fb8f2,#0b7bc8);display:flex;align-items:center;justify-content:center;box-shadow:0 2px 3px rgba(0,0,0,.3)}
/* markets */
.market{top:465px;width:190px}
.market-icon{width:80px;height:80px;border-radius:8px;background:radial-gradient(#e8eaee,#a9aeb7)}
.market h2{font-family:"Noto Sans",sans-serif;font-weight:400;font-size:14px;color:var(--heading);margin-top:14px}
.market p{font-family:"Noto Sans",sans-serif;font-size:12px;line-height:16px;color:var(--muted);margin-top:4px}
.market .btn-small{width:81px;height:20px;font-size:9.5px;border-radius:10px;margin-top:27px}
.divider{top:520px;width:2px;height:95px;background:linear-gradient(#fff,#ddd,#fff)}
/* setups */
.section-title{font-family:"Gelasio",serif;font-weight:400;font-size:16.5px;color:var(--heading);white-space:nowrap}
.section-title span{color:var(--sky)}
.setups-title{left:49px;top:696px;width:602px;padding-bottom:8px;border-bottom:1px dashed #aaa}
.thumb{top:751px;width:137px;height:106px;border:2px solid #111}
.scroller{left:47px;top:878px;width:598px;height:25px;border-radius:12px;background:linear-gradient(#7fd0fa,#149be6);border:1px solid #0c7cc0}
.scroller-track{left:24px;top:2px;width:548px;height:19px;border-radius:10px;background:linear-gradient(#4ab7f0,#1a9ae0);border:1px solid #0e84c8}
.scroller-thumb{left:62px;top:1px;width:70px;height:16px;border-radius:8px;background:linear-gradient(#b6e6fd,#6ccaf6)}
.scroller-shadow{left:52px;top:903px;width:588px;height:14px;background:linear-gradient(#8aa4bf,rgba(255,255,255,0));opacity:.6}
/* queries */
.queries-title{left:678px;top:696px;width:230px;padding-bottom:8px;border-bottom:1px dashed #aaa;font-size:15.5px}
.field{left:678px;width:232px;border:1px solid #b7c7d8;background:#fff;font-size:9px;color:#777;padding:7px}
.submit{left:678px;top:880px;width:71px;height:22px;background:linear-gradient(#45b6f3,#0e82cf);color:#fff;font-size:12px;display:flex;align-items:center;justify-content:center}
/* footer */
.footer{left:0;top:945px;width:940px;height:172px;background:linear-gradient(var(--navy),var(--navy-deep))}
.footer-title{font-family:"Gelasio",serif;font-weight:400;font-size:16.5px;color:#fff}
.quick{left:74px;top:990px;list-style:none}
.quick li{font-family:"Gelasio",serif;font-size:10.5px;color:#57c2f5;height:20.5px;position:relative}
.quick li::before{content:"";position:absolute;left:-13px;top:4px;border-left:5px solid #57c2f5;border-top:3px solid transparent;border-bottom:3px solid transparent}
.news-input{left:331px;top:1003px;width:226px;height:30px;border-radius:7px;background:linear-gradient(#d2d2d2,#e4e4e4);border:2px solid #fff;font-size:9.5px;color:#444;padding:8px 6px}
.signup{left:331px;top:1040px;width:77px;height:26px;border-radius:8px;background:linear-gradient(#5dc2f7,#0f84d2);border:1px solid #8fd8fb;color:#fff;font-weight:700;font-size:12px;display:flex;align-items:center;justify-content:center}
.news-box{left:645px;top:985px;width:260px;height:82px;border-radius:6px;background:#fff;border:2px solid #c6d6ea;padding:10px 10px}
.news-box::before{content:"";position:absolute;left:98px;top:-9px;border-left:9px solid transparent;border-right:9px solid transparent;border-bottom:9px solid #fff}
.news-box p{font-size:8.6px;line-height:12px;color:#333}
.news-meta{display:flex;justify-content:space-between;font-size:9px;font-weight:700;margin-top:8px;color:#333}
.news-meta span{color:#1a7fd4}
.foot-rule{left:45px;top:1078px;width:862px;height:1px;background:#2d4b84}
.foot-links{left:57px;top:1090px;display:flex;font-size:9px;color:#fff;white-space:nowrap}
.foot-links span{padding:0 7px;border-left:1px solid #fff;line-height:10px}
.foot-links span:first-child{padding-left:0;border:0}
.copyright{left:790px;top:1090px;font-size:9px;color:#fff;white-space:nowrap}
</style>
</head>
<body>
<div class="page">

  <header>
    <div class="abs brand"><div class="brand-mark"></div><div class="brand-name">Bright Harbor<small>Lighting Systems</small></div></div>
    <div class="abs quote-btn">REQUEST A QUOTE
      <svg viewBox="0 0 18 18"><circle cx="9" cy="9" r="7.5" fill="none" stroke="#fff" stroke-width="1.5"/><path d="M5 9h7M9 6l3 3-3 3" fill="none" stroke="#fff" stroke-width="1.5"/></svg>
    </div>
    <div class="abs phone">
      <svg width="30" height="38" viewBox="0 0 30 38"><rect x="3" y="14" width="24" height="22" rx="3" fill="#bfc3c8" stroke="#777"/><rect x="9" y="2" width="11" height="20" rx="3" fill="#555"/><rect x="11" y="6" width="7" height="5" fill="#9fd0ee"/><g fill="#eee"><rect x="7" y="25" width="4" height="3"/><rect x="13" y="25" width="4" height="3"/><rect x="19" y="25" width="4" height="3"/><rect x="7" y="30" width="4" height="3"/><rect x="13" y="30" width="4" height="3"/><rect x="19" y="30" width="4" height="3"/></g></svg>
      (01555) 382914
    </div>
  </header>

  <nav class="abs nav">
    <a class="active" style="width:74px">Home</a>
    <a style="width:82px">Why Us?</a>
    <a style="width:80px">Resume</a>
    <a style="width:84px">Products</a>
    <a style="width:204px">Lighting Design/Quote Request</a>
    <a style="width:86px">About Us</a>
    <a style="width:82px">Manuals</a>
    <a style="width:89px">Technical</a>
    <a style="width:90px">Contact Us</a>
  </nav>
  <div class="abs nav-rule"></div>

  <section class="abs welcome">
    <h1>Welcome to <span>Bright Harbor Lighting Systems</span></h1>
    <p class="pedigree"><span class="lead">Pedigree:</span> <span class="claim">Engineered for performance, the type that ASTRA demands.</span></p>
    <p class="body">Bright Harbor Lighting's studio and video fluorescent fixtures are born from a heritage of advanced technology optics research and solar collection/ reflection design and engineering expertise.</p>
    <p class="body">Bright Harbor Lighting's founding parent company, Helion Optics, was selected by ASTRA to design and manufacture optical systems for the space station. Engineers design our flo lights for optimal spectral performance and superior subject illumination. If ASTRA can trust our engineers, just think what we can do for your lighting project!</p>
  </section>
  <div class="abs welcome-rule"></div>
  <div class="abs btn-small read-more">&#9656; read more</div>

  <div class="abs slider">
    <div class="abs slide-photo" role="img" aria-label="Television studio set lit with wood panels and a news desk"></div>
  </div>
  <div class="abs arrow" style="left:404px"><svg width="20" height="22"><path d="M16 2L3 11l13 9z" fill="#0b4f8f"/></svg></div>
  <div class="abs arrow" style="left:859px"><svg width="20" height="22"><path d="M4 2l13 9-13 9z" fill="#0b4f8f"/></svg></div>

  <section>
    <div class="abs market" style="left:53px">
      <div class="market-icon" style="margin-left:12px" role="img" aria-label="Satellite dish illustration"></div>
      <h2>Broadcasting</h2><p>Lorem ipsum dolor sit amet, consectetur adipiscing elit.</p>
      <div class="btn-small">Learn More</div>
    </div>
    <div class="abs divider" style="left:245px"></div>
    <div class="abs market" style="left:286px">
      <div class="market-icon" style="margin-left:18px" role="img" aria-label="Graduate in cap and gown illustration"></div>
      <h2>Education</h2><p>Lorem ipsum dolor sit amet, consectetur adipiscing elit.</p>
      <div class="btn-small">Learn More</div>
    </div>
    <div class="abs divider" style="left:470px"></div>
    <div class="abs market" style="left:514px">
      <div class="market-icon" style="margin-left:4px" role="img" aria-label="Newspaper with globe illustration"></div>
      <h2>Government</h2><p>Lorem ipsum dolor sit amet, consectetur adipiscing elit.</p>
      <div class="btn-small">Learn More</div>
    </div>
    <div class="abs divider" style="left:702px"></div>
    <div class="abs market" style="left:755px">
      <div class="market-icon" style="width:92px" role="img" aria-label="Video camcorder illustration"></div>
      <h2>Religious</h2><p>Lorem ipsum dolor sit amet, consectetur adipiscing elit.</p>
      <div class="btn-small">Learn More</div>
    </div>
  </section>

  <h2 class="abs section-title setups-title">Some of our Great Lighting Setups</h2>
  <div class="abs thumb" style="left:54px;background:linear-gradient(#1a1f2a,#3d6a8a 50%,#6b4a2a)" role="img" aria-label="Studio set with bookshelves under lights"></div>
  <div class="abs thumb" style="left:203px;background:linear-gradient(#111,#3b4f6e 55%,#20242c)" role="img" aria-label="Newsroom lighting grid"></div>
  <div class="abs thumb" style="left:353px;background:linear-gradient(#2a2118,#7a5a3a 50%,#3a3026)" role="img" aria-label="Studio with camera and warm lighting"></div>
  <div class="abs thumb" style="left:502px;background:linear-gradient(#5a3a22,#a0704a 45%,#3a1e10)" role="img" aria-label="Conference room with video screen"></div>
  <div class="abs scroller-shadow"></div>
  <div class="abs scroller">
    <svg class="abs" style="left:6px;top:5px" width="12" height="14"><path d="M9 2L3 7l6 5" fill="none" stroke="#fff" stroke-width="2.5"/></svg>
    <div class="abs scroller-track"><div class="abs scroller-thumb"></div></div>
    <svg class="abs" style="right:6px;top:5px" width="12" height="14"><path d="M3 2l6 5-6 5" fill="none" stroke="#fff" stroke-width="2.5"/></svg>
  </div>

  <h2 class="abs section-title queries-title">Any Queries? <span>Feel Free to Ask</span></h2>
  <div class="abs field" style="top:737px;height:23px">Your Name</div>
  <div class="abs field" style="top:766px;height:23px">Your Email id</div>
  <div class="abs field" style="top:795px;height:80px;padding-top:12px">Your Question</div>
  <div class="abs submit">Submit</div>

  <footer class="abs footer"></footer>
  <h3 class="abs footer-title" style="left:52px;top:957px">Quick links</h3>
  <ul class="abs quick"><li>Fixture cutsheets</li><li>Cost saving calculator</li><li>Customer List</li></ul>
  <h3 class="abs footer-title" style="left:335px;top:958px">Subscribe Newsletter</h3>
  <div class="abs news-input">Your email id</div>
  <div class="abs signup">SIGN UP</div>
  <h3 class="abs footer-title" style="left:651px;top:954px">Latest News</h3>
  <div class="abs news-box">
    <p>Lorem ipsum dolor sit amet, consectetur adipiscing elit. Quisque consectetur ultrices semper. Class aptent taciti sociosqu ad litora torquent per conubia nostra</p>
    <div class="news-meta">06:00 PM Nov 03rd, 2011<span>More News</span></div>
  </div>
  <div class="abs foot-rule"></div>
  <div class="abs foot-links"><span>Home</span><span>Why Us?</span><span>Resume</span><span>Products</span><span>Lighting Design/Quote Request</span><span>About Us</span><span>Manuals</span><span>Technical</span><span>Contact Us</span></div>
  <div class="abs copyright">© 2012, All Rights Reserved</div>

</div>
</body>
</html>
```